Rollers & Glides.com

Vertical Business Card with focus on branding with our icon. Information on card will be logo, persons name, position, phone number, email address and website. Use the the name Marcus Tilden, position President, phone number 555.214.8890, email Marcus@rollersandglides.com, website www.rollersandglides.com.

```html
<!DOCTYPE html>
<html lang="en">
<head>
<meta charset="UTF-8">
<title>Rollers & Glides — Business Card</title>
<link rel="stylesheet" href="https://fonts.googleapis.com/css2?family=Montserrat:wght@300;400;700&display=swap">
<style>
  :root {
    --backdrop: #3e4149;
    --ink: #0a0a0a;
    --paper: #f2f2f2;
    --paper-text: #ffffff;
    --muted: #2a2a2a;
  }
  * { box-sizing: border-box; margin: 0; padding: 0; }
  html, body {
    width: 1200px; height: 971px; overflow: hidden;
    background: var(--backdrop);
    font-family: "Montserrat", sans-serif;
  }
  .stage {
    position: relative; width: 1200px; height: 971px;
    display: flex; justify-content: center; align-items: center; gap: 90px;
  }
  .card {
    width: 310px; height: 560px;
    display: flex; flex-direction: column; align-items: center;
    box-shadow: 0 10px 30px rgba(0,0,0,.35);
  }
  .card > * { flex-shrink: 0; }
  .card--front { background: var(--ink); color: var(--paper-text); justify-content: center; }
  .card--back { background: var(--paper); color: var(--ink); padding: 46px 0 40px; }

  .brand-mark {
    display: block; flex-shrink: 0;
    width: 84px; height: 84px; border-radius: 50%;
  }
  .card--front .brand-mark { background: var(--paper-text); }
  .card--back .brand-mark { background: var(--ink); }
  .brand-name {
    margin-top: 20px; font-weight: 700; font-size: 17px; letter-spacing: .5px;
  }

  .person { margin-top: 72px; text-align: center; }
  .person__name { font-size: 26px; letter-spacing: .5px; line-height: 1.2; }
  .person__first { font-weight: 700; }
  .person__last { font-weight: 300; }
  .person__role { font-weight: 300; font-size: 17px; margin-top: 2px; color: var(--muted); }

  .contact-icons { display: flex; gap: 12px; margin-top: 26px; }
  .contact-icon {
    width: 22px; height: 22px; border-radius: 50%; background: var(--ink);
    display: flex; align-items: center; justify-content: center; flex-shrink: 0;
  }
  .contact-icon svg { width: 13px; height: 13px; }

  .contact-list { list-style: none; text-align: center; margin-top: 18px; font-size: 12.5px; line-height: 1.65; }

  .divider { position: relative; width: 140px; height: 22px; margin-top: 16px; }
  .divider::before {
    content: ""; position: absolute; left: 0; right: 0; top: 50%; height: 1px; background: var(--ink);
  }
  .divider .contact-icon { position: absolute; left: 50%; top: 0; transform: translateX(-50%); }

  .address { margin-top: 10px; text-align: center; font-size: 11px; line-height: 1.7; font-style: normal; }
</style>
</head>
<body>
<main class="stage">
  <section class="card card--front" aria-label="Card front">
    <span class="brand-mark" aria-hidden="true"></span>
    <p class="brand-name">ROLLERSANDGLIDES</p>
  </section>

  <section class="card card--back" aria-label="Card back">
    <span class="brand-mark" aria-hidden="true"></span>
    <p class="brand-name">ROLLERSANDGLIDES</p>

    <div class="person">
      <h1 class="person__name"><span class="person__first">MARCUS</span> <span class="person__last">TILDEN</span></h1>
      <p class="person__role">President</p>
    </div>

    <div class="contact-icons">
      <span class="contact-icon">
        <svg viewBox="0 0 24 24" fill="none" stroke="#fff" stroke-width="2" stroke-linecap="round" stroke-linejoin="round"><path d="M6 3h4l2 5-2.5 1.5a11 11 0 0 0 5 5L16 12l5 2v4a2 2 0 0 1-2 2A16 16 0 0 1 4 5a2 2 0 0 1 2-2z"/></svg>
      </span>
      <span class="contact-icon">
        <svg viewBox="0 0 24 24" fill="none" stroke="#fff" stroke-width="2" stroke-linejoin="round"><rect x="3" y="5" width="18" height="14" rx="1"/><path d="M3 6l9 7 9-7"/></svg>
      </span>
      <span class="contact-icon">
        <svg viewBox="0 0 24 24" fill="none" stroke="#fff" stroke-width="1.8"><circle cx="12" cy="12" r="9"/><path d="M3 12h18M12 3c3 3 3 15 0 18M12 3c-3 3-3 15 0 18"/></svg>
      </span>
    </div>

    <ul class="contact-list">
      <li>555-214-8890</li>
      <li>marcus@rollersandglides.com</li>
      <li>www.rollersandglides.com</li>
    </ul>

    <div class="divider">
      <span class="contact-icon">
        <svg viewBox="0 0 24 24" fill="none" stroke="#fff" stroke-width="2" stroke-linejoin="round"><path d="M3 11l9-7 9 7M5 10v10h14V10"/></svg>
      </span>
    </div>

    <address class="address">
      1480 Harbor Crest Ave,<br>
      Lakeview, ON K4R 2T9,<br>
      USA
    </address>
  </section>
</main>
</body>
</html>
```